Business card - Brio Margin - size 85 mm * 55 mm

We need new business cards. Design must fit with our vision of the firm. You find in the attached file our logo and a short description of our firm (mission, vision, value, business and so on).

Target Market(s)

Consulting firm in performance improvement

Industry/Entity Type

Management Consulting

Contact Information for Business Card

SIZE
85 mm * 55 mm
INFORMATIONS
name surname
role position
telephone number
email address

Requirements
Must have
• the brand must APPEAR for the rest Would we like to have something sleek, inspired to a "just right" approach
Should not have
• Please avoid the black color as background

```html
<!DOCTYPE html>
<html lang="en">
<head>
<meta charset="utf-8">
<title>Brio Margin – Business Card</title>
<link href="https://fonts.googleapis.com/css2?family=Questrial&family=Source+Sans+3:wght@400;600&display=swap" rel="stylesheet">
<style>
  :root {
    --stage: #ecebe9;
    --brand-orange: #ff6a00;
    --card-dark: #3d3d3d;
    --watermark: #363636;
    --paper: #ffffff;
    --ring-tint: #cfe0d6;
  }
  html, body {
    margin: 0;
    width: 1200px;
    height: 900px;
    overflow: hidden;
    background: var(--stage);
  }
  .canvas {
    position: relative;
    width: 1200px;
    height: 900px;
  }
  .card {
    position: absolute;
    overflow: hidden;
    box-shadow: 0 6px 18px rgba(0,0,0,0.18);
  }
  /* Front */
  .card--front {
    left: 238px;
    top: 62px;
    width: 555px;
    height: 343px;
    background: var(--brand-orange);
    color: var(--paper);
  }
  .wordmark {
    position: absolute;
    left: 0;
    right: 0;
    top: 66px;
    margin: 0;
    text-align: center;
    font-family: "Questrial", sans-serif;
    font-weight: 400;
    font-size: 44px;
    letter-spacing: 0.42em;
    padding-left: 0.42em;
    text-transform: uppercase;
    color: var(--paper);
  }
  .person {
    position: absolute;
    left: 44px;
    top: 172px;
    font-family: "Source Sans 3", sans-serif;
  }
  .person__name {
    margin: 0;
    font-size: 18px;
    font-weight: 600;
    line-height: 1.2;
  }
  .person__role {
    margin: 2px 0 0;
    font-size: 14.5px;
    font-weight: 400;
  }
  .contact {
    position: absolute;
    left: 44px;
    top: 255px;
    margin: 0;
    padding: 0;
    list-style: none;
    font-family: "Source Sans 3", sans-serif;
    font-size: 14.5px;
  }
  .contact__item {
    display: flex;
    align-items: center;
    gap: 8px;
    height: 20px;
  }
  .contact__icon {
    width: 12px;
    height: 12px;
    fill: var(--paper);
  }
  .brand-badge {
    position: absolute;
    left: 320px;
    top: 148px;
    width: 190px;
    height: 190px;
    border-radius: 50%;
    background: var(--paper);
    display: flex;
    align-items: center;
    justify-content: center;
  }
  .brand-badge__name {
    font-family: "Questrial", sans-serif;
    font-size: 22px;
    color: var(--brand-orange);
    letter-spacing: 0.04em;
  }
  /* Back */
  .card--back {
    left: 458px;
    top: 516px;
    width: 559px;
    height: 342px;
    background: var(--card-dark);
  }
  .back__watermark {
    position: absolute;
    left: 40px;
    top: 148px;
    width: 180px;
    height: 180px;
    border-radius: 50%;
    border: 14px solid var(--watermark);
    box-sizing: border-box;
  }
  .back__ring {
    position: absolute;
    left: 232px;
    top: 68px;
    width: 128px;
    height: 128px;
    border-radius: 50%;
    border: 5px solid var(--brand-orange);
    box-sizing: border-box;
  }
  .back__wordmark {
    position: absolute;
    left: 164px;
    top: 216px;
    margin: 0;
    font-family: "Questrial", sans-serif;
    font-size: 25px;
    letter-spacing: 0.36em;
    text-transform: uppercase;
    color: var(--brand-orange);
  }
</style>
</head>
<body>
<main class="canvas">
  <section class="card card--front" aria-label="Business card front">
    <h1 class="wordmark">Brio Margin</h1>
    <div class="person">
      <p class="person__name">Elias Varden</p>
      <p class="person__role">Managing Director</p>
    </div>
    <ul class="contact">
      <li class="contact__item">
        <svg class="contact__icon" viewBox="0 0 24 24" aria-hidden="true"><path d="M6.6 10.8a15.1 15.1 0 0 0 6.6 6.6l2.2-2.2a1 1 0 0 1 1-.25 11.4 11.4 0 0 0 3.6.57 1 1 0 0 1 1 1V20a1 1 0 0 1-1 1A17 17 0 0 1 3 4a1 1 0 0 1 1-1h3.5a1 1 0 0 1 1 1c0 1.25.2 2.45.57 3.57a1 1 0 0 1-.25 1z"/></svg>
        <span>031-555 204 718</span>
      </li>
      <li class="contact__item">
        <svg class="contact__icon" viewBox="0 0 24 24" aria-hidden="true"><path d="M3 6h18v12H3z M3 6l9 7 9-7" fill="none" stroke="#fff" stroke-width="2.4"/></svg>
        <span>hello@briomargin.com</span>
      </li>
    </ul>
    <div class="brand-badge"><span class="brand-badge__name">Brio Margin</span></div>
  </section>

  <section class="card card--back" aria-label="Business card back">
    <div class="back__watermark" aria-hidden="true"></div>
    <div class="back__ring" aria-hidden="true"></div>
    <p class="back__wordmark">Brio Margin</p>
  </section>
</main>
</body>
</html>
```